Postcard Design Project

We are a small printing company specializing in envelope printing.
We market to churches and medical offices.

Industry/Entity Type

It Company

```html
<!DOCTYPE html>
<html lang="en">
<head>
<meta charset="utf-8">
<title>Halden Print – Envelope Printing Postcard</title>
<link href="https://fonts.googleapis.com/css2?family=Titillium+Web:wght@700;900&family=Catamaran:wght@500;700&display=swap" rel="stylesheet">
<style>
  :root {
    --teal-light: #27b3ad;
    --teal: #0fa1a0;
    --teal-deep: #0a8a96;
    --blue-corner: #2f7fb8;
    --white: #ffffff;
    --yellow: #e8e52a;
    --ink: #0b0b0b;
    --band-orange: #f1b233;
    --band-yellow: #e6e52c;
  }
  * { margin: 0; padding: 0; box-sizing: border-box; }
  html, body { width: 816px; height: 1200px; overflow: hidden; background: var(--teal); }
  .postcard {
    position: relative;
    width: 816px;
    height: 1200px;
    overflow: hidden;
    background:
      radial-gradient(ellipse at 95% 0%, var(--blue-corner) 0%, transparent 40%),
      radial-gradient(ellipse at 10% 30%, rgba(255,255,255,0.18) 0%, transparent 45%),
      linear-gradient(180deg, var(--teal-light) 0%, var(--teal) 55%, var(--teal-deep) 100%);
    font-family: "Catamaran", sans-serif;
    color: var(--ink);
  }
  .headline {
    position: absolute;
    top: 40px;
    left: 0;
    width: 100%;
    text-align: center;
    font-family: "Titillium Web", sans-serif;
    font-weight: 900;
    line-height: 1;
  }
  .headline__lead { color: var(--white); font-size: 58px; letter-spacing: -0.5px; }
  .headline__question {
    color: var(--yellow);
    font-size: 45px;
    font-weight: 700;
    line-height: 58px;
    margin-top: 6px;
    letter-spacing: -0.5px;
  }
  .brand-name {
    position: absolute;
    top: 286px;
    left: 0;
    width: 100%;
    text-align: center;
    font-family: "Titillium Web", sans-serif;
    font-weight: 900;
    font-size: 108px;
    line-height: 1.1;
    color: var(--ink);
  }
  .tagline {
    position: absolute;
    top: 438px;
    left: 0;
    width: 100%;
    text-align: center;
    font-family: "Catamaran", sans-serif;
    font-weight: 500;
    font-size: 35px;
    line-height: 46px;
    color: var(--ink);
  }
  .product-photo {
    position: absolute;
    left: 0;
    top: 660px;
    width: 816px;
    height: 428px;
  }
  .services {
    position: absolute;
    left: 22px;
    top: 570px;
    width: 496px;
    height: 270px;
    background: var(--yellow);
    border-radius: 20px;
    padding: 20px 0 0 46px;
  }
  .services__list { list-style: none; }
  .services__item {
    position: relative;
    padding-left: 20px;
    font-family: "Titillium Web", sans-serif;
    font-weight: 700;
    font-size: 27px;
    line-height: 41.6px;
    color: var(--ink);
  }
  .services__item::before {
    content: "";
    position: absolute;
    left: 2px;
    top: 18px;
    width: 8px;
    height: 8px;
    border-radius: 50%;
    background: var(--ink);
  }
  .services__note {
    position: absolute;
    right: 28px;
    bottom: 22px;
    font-family: "Catamaran", sans-serif;
    font-weight: 500;
    font-size: 19px;
    color: var(--ink);
  }
  .contact-band {
    position: absolute;
    left: 0;
    top: 1088px;
    width: 816px;
    height: 112px;
  }
  .contact-band__shape { position: absolute; inset: 0; width: 100%; height: 100%; }
  .contact-band__text {
    position: absolute;
    inset: 0;
    text-align: center;
    font-family: "Catamaran", sans-serif;
    font-weight: 700;
    font-size: 31px;
    line-height: 48px;
    padding-top: 10px;
    color: var(--ink);
  }
</style>
</head>
<body>
<main class="postcard">
  <header class="headline">
    <div class="headline__lead">WHAT DO YOU DO</div>
    <div class="headline__question">When You’re Down To Your<br>Last Box of Envelopes ?</div>
  </header>

  <h1 class="brand-name">Halden Print</h1>

  <p class="tagline">Will Give You Solution For Fast,<br>Economical, Quality Envelopes.</p>

  <svg class="product-photo" role="img" aria-label="Photo of stacked printed envelopes: a business envelope with blue flap, a church offering envelope and a stack of grey-flapped offering envelopes" viewBox="0 0 816 428">
    <defs>
      <linearGradient id="envelopeTones" x1="0" y1="0" x2="1" y2="1">
        <stop offset="0" stop-color="#e9eef0"/>
        <stop offset="0.5" stop-color="#cfd6d8"/>
        <stop offset="1" stop-color="#9aa4a6"/>
      </linearGradient>
    </defs>
    <polygon points="0,120 360,250 310,420 0,420" fill="url(#envelopeTones)" opacity="0.9"/>
    <polygon points="420,250 640,0 816,10 816,428 350,428" fill="url(#envelopeTones)" opacity="0.9"/>
  </svg>

  <section class="services">
    <ul class="services__list">
      <li class="services__item">Custom Business Envelopes</li>
      <li class="services__item">Church Offering Envelopes</li>
      <li class="services__item">Free Copy Changes</li>
      <li class="services__item">Medical Billing Envelopes</li>
      <li class="services__item">Free Shipping</li>
    </ul>
    <span class="services__note">* Variety of Paper and Size</span>
  </section>

  <footer class="contact-band">
    <svg class="contact-band__shape" viewBox="0 0 816 112" preserveAspectRatio="none" aria-hidden="true">
      <rect width="816" height="112" fill="var(--band-orange)"/>
      <polygon points="0,20 110,112 0,112" fill="var(--band-yellow)"/>
      <polygon points="816,10 700,112 816,112" fill="var(--band-yellow)"/>
    </svg>
    <div class="contact-band__text">
      Call for a free estimate 555-014-2790<br>
      E-mail : hello@haldenprint.example
    </div>
  </footer>
</main>
</body>
</html>
```